Letterhead Design Project

Please do not submit designs until I upload file-

Requirements
Must have
• clean lines and font- easy to read; consistent with the design on the business card
Does not use too much of the real estate of the size of the paper

```html
<!DOCTYPE html>
<html lang="en">
<head>
<meta charset="utf-8">
<title>Alder Ridge Foundation – Letterhead</title>
<link href="https://fonts.googleapis.com/css2?family=Montserrat:wght@400;700&display=swap" rel="stylesheet">
<style>
  :root {
    --backdrop: #ececec;
    --paper: #f7f7f7;
    --navy: #1f3a68;
    --ink: #4a4d52;
    --icon: #6d7f9e;
  }
  * { box-sizing: border-box; margin: 0; padding: 0; }
  html, body {
    width: 1200px;
    height: 795px;
    overflow: hidden;
    background: var(--backdrop);
  }
  .canvas {
    width: 1200px;
    height: 795px;
    display: flex;
    align-items: center;
    justify-content: center;
  }
  .letterhead {
    position: relative;
    width: 530px;
    height: 750px;
    background: var(--paper);
    box-shadow: 0 2px 10px rgba(0, 0, 0, 0.08);
    font-family: "Montserrat", sans-serif;
    color: var(--ink);
  }
  .brand {
    position: absolute;
    top: 54px;
    left: 52px;
    display: flex;
    align-items: center;
    gap: 10px;
  }
  .brand-square {
    width: 16px;
    height: 16px;
    background: var(--navy);
  }
  .brand-name {
    font-weight: 700;
    font-size: 13px;
    line-height: 1.1;
    letter-spacing: 0.06em;
    text-transform: uppercase;
    color: var(--navy);
  }
  .contact {
    position: absolute;
    top: 50px;
    right: 52px;
    font-size: 8px;
    line-height: 1.75;
    letter-spacing: 0.08em;
  }
  .contact-address { margin-bottom: 6px; }
  .contact-line {
    display: flex;
    align-items: center;
    gap: 7px;
  }
  .contact-line svg {
    width: 8px;
    height: 8px;
    flex: none;
  }
</style>
</head>
<body>
  <main class="canvas">
    <section class="letterhead">
      <header class="brand">
        <span class="brand-square"></span>
        <span class="brand-name">The<br>Alder Ridge<br>Foundation</span>
      </header>

      <address class="contact" style="font-style: normal;">
        <p class="contact-address">1450 Harbor Point Drive, Suite 310<br>Clearwater Bay, FL 33760</p>
        <p class="contact-line">
          <svg viewBox="0 0 10 10" aria-hidden="true"><path d="M2 1h2l1 2.5-1.3.8a5 5 0 0 0 2 2l.8-1.3L9 6v2a1 1 0 0 1-1 1A7 7 0 0 1 1 2a1 1 0 0 1 1-1z" fill="none" stroke="var(--icon)" stroke-width="0.9"/></svg>
          +1 555-014-2280
        </p>
        <p class="contact-line">
          <svg viewBox="0 0 10 10" aria-hidden="true"><rect x="0.5" y="2" width="9" height="6" fill="var(--icon)"/><path d="M0.5 2l4.5 3.5L9.5 2" fill="none" stroke="var(--paper)" stroke-width="0.8"/></svg>
          j.ellis@alderridgefoundation.org
        </p>
        <p class="contact-line">
          <svg viewBox="0 0 10 10" aria-hidden="true"><circle cx="5" cy="5" r="4.3" fill="none" stroke="var(--icon)" stroke-width="0.9"/><ellipse cx="5" cy="5" rx="1.8" ry="4.3" fill="none" stroke="var(--icon)" stroke-width="0.7"/><path d="M0.7 5h8.6" stroke="var(--icon)" stroke-width="0.7"/></svg>
          www.alderridgefoundation.org
        </p>
      </address>
    </section>
  </main>
</body>
</html>
```